Disposable Mini Sauce Pot Design for Asian Chain Food Brands

We operate a Hainan Chicken Rice takeout brand under the name Spin4Rye, with our official website: www.Spin4Rye.com.
We offer four signature house sauces and are launching brand-new packaging for our sauce line. We require custom graphic designs exclusively for the sauce cup lids.
Product Material & Base Specs
The sauce cups are made of PP plastic, available in two translucent base options: Translucent White and Translucent Orange.
Four Sauce Varieties for Individual Lid Designs
1. Red Sauce – Fried Sweet Chili Sauce
2.Green Sauce – Scallion Oil Dressing
3.Sweet Soy Sauce
4.Sweet Red Sauce (Special for Fried Chicken)
Differentiate each sauce lid design through unique graphics, typography, or illustrative elements for easy customer identification.
The marking NET WT 2 OZ must be clearly printed on every lid.
**There is no need to print full descriptive text or the full name of the sauces on each lid; the design only needs to clearly differentiate the four sauce varieties.
**Please reference the original design style and brand color palette shown on our official website, and feel free to fully unleash your creativity.

```html
<!DOCTYPE html>
<html lang="en">
<head>
<meta charset="utf-8">
<title>Spin4Rye Sauce Lids</title>
<link href="https://fonts.googleapis.com/css2?family=Bowlby+One&family=Chewy&family=Baloo+2:wght@600&display=swap" rel="stylesheet">
<style>
  :root {
    --red: #ec1c24;
    --green: #6e8436;
    --soy: #9b1b1f;
    --black: #0b0b0b;
    --ink: #ffffff;
    --page: #ffffff;
  }
  html, body {
    margin: 0;
    width: 1200px;
    height: 559px;
    overflow: hidden;
    background: var(--page);
  }
  .lid-row {
    position: relative;
    width: 1200px;
    height: 559px;
  }
  .lid {
    position: absolute;
    top: 126px;
    width: 272px;
    height: 307px;
  }
  .lid--red { left: 28px; }
  .lid--green { left: 319px; }
  .lid--soy { left: 610px; }
  .lid--black { left: 901px; }
  .headline { font-family: "Bowlby One", "Arial Black", sans-serif; fill: var(--ink); }
  .headline--accent { fill: var(--red); }
  .weight { font-family: "Bowlby One", "Arial Black", sans-serif; fill: var(--ink); }
  .weight--accent { fill: var(--red); }
  .website { font-family: "Baloo 2", sans-serif; font-weight: 600; fill: var(--ink); }
  .bubble-text { font-family: "Chewy", cursive; fill: var(--ink); }
  .brand-text { font-family: "Bowlby One", "Arial Black", sans-serif; }
</style>
</head>
<body>
<main class="lid-row">

  <!-- Red Sauce -->
  <svg class="lid lid--red" viewBox="0 0 272 307" aria-label="Red Sauce lid">
    <rect width="272" height="307" rx="32" fill="var(--red)"/>
    <text class="headline" x="29" y="91" font-size="80" textLength="56" lengthAdjust="spacingAndGlyphs">R</text>
    <text class="headline" x="31" y="152" font-size="80" textLength="52" lengthAdjust="spacingAndGlyphs">E</text>
    <text class="headline" x="31" y="222" font-size="80" textLength="54" lengthAdjust="spacingAndGlyphs">D</text>
    <line x1="91" y1="30" x2="91" y2="236" stroke="var(--ink)" stroke-width="1"/>
    <text class="headline" x="97" y="84" font-size="76" textLength="148" lengthAdjust="spacingAndGlyphs">SAU</text>
    <text class="headline" x="99" y="181" font-size="122" textLength="146" lengthAdjust="spacingAndGlyphs">CE</text>
    <rect x="96" y="190" width="84" height="46" rx="18" fill="var(--ink)" opacity="0.9" role="img" aria-label="Two chick illustrations"/>
    <ellipse cx="214" cy="205" rx="27" ry="19" fill="none" stroke="var(--ink)" stroke-width="1.6"/>
    <text class="bubble-text" x="214" y="202" font-size="12" text-anchor="middle">The</text>
    <text class="bubble-text" x="214" y="215" font-size="12" text-anchor="middle">Original</text>
    <text class="weight" x="29" y="268" font-size="27" textLength="149" lengthAdjust="spacingAndGlyphs">NET WT 2 OZ</text>
    <line x1="29" y1="271" x2="190" y2="271" stroke="var(--ink)" stroke-width="1"/>
    <text class="website" x="29" y="286" font-size="11" textLength="149" lengthAdjust="spacing">www.Spin4Rye.com</text>
    <circle cx="216" cy="263" r="25" fill="var(--ink)"/>
    <text class="brand-text" x="216" y="267" font-size="10" text-anchor="middle" fill="var(--red)">Spin4Rye</text>
  </svg>

  <!-- Green Sauce -->
  <svg class="lid lid--green" viewBox="0 0 272 307" aria-label="Green Sauce lid">
    <rect width="272" height="307" rx="32" fill="var(--green)"/>
    <text class="headline" x="29" y="88" font-size="84" textLength="156" lengthAdjust="spacingAndGlyphs">GRE</text>
    <text class="headline" x="31" y="186" font-size="128" textLength="152" lengthAdjust="spacingAndGlyphs">EN</text>
    <line x1="193" y1="28" x2="193" y2="232" stroke="var(--ink)" stroke-width="1"/>
    <text class="headline" transform="translate(203 28) rotate(90)" x="0" y="0" font-size="58" textLength="198" lengthAdjust="spacingAndGlyphs">SAUCE</text>
    <ellipse cx="59" cy="212" rx="27" ry="19" fill="none" stroke="var(--ink)" stroke-width="1.6"/>
    <text class="bubble-text" x="59" y="209" font-size="12" text-anchor="middle">The</text>
    <text class="bubble-text" x="59" y="222" font-size="12" text-anchor="middle">Original</text>
    <rect x="96" y="190" width="84" height="46" rx="18" fill="var(--ink)" opacity="0.9" role="img" aria-label="Two chick illustrations"/>
    <text class="weight" x="29" y="268" font-size="27" textLength="149" lengthAdjust="spacingAndGlyphs">NET WT 2 OZ</text>
    <line x1="29" y1="271" x2="190" y2="271" stroke="var(--ink)" stroke-width="1"/>
    <text class="website" x="29" y="286" font-size="11" textLength="149" lengthAdjust="spacing">www.Spin4Rye.com</text>
    <circle cx="216" cy="263" r="25" fill="var(--ink)"/>
    <text class="brand-text" x="216" y="267" font-size="10" text-anchor="middle" fill="var(--green)">Spin4Rye</text>
  </svg>

  <!-- Sweet Soy Sauce -->
  <svg class="lid lid--soy" viewBox="0 0 272 307" aria-label="Sweet Soy Sauce lid">
    <rect width="272" height="307" rx="32" fill="var(--soy)"/>
    <text class="headline" x="33" y="74" font-size="62" textLength="214" lengthAdjust="spacingAndGlyphs">SWEET</text>
    <text class="headline" x="35" y="146" font-size="94" textLength="210" lengthAdjust="spacingAndGlyphs">SOY</text>
    <text class="headline" x="33" y="189" font-size="54" textLength="212" lengthAdjust="spacingAndGlyphs">SAUCE</text>
    <ellipse cx="60" cy="212" rx="27" ry="19" fill="none" stroke="var(--ink)" stroke-width="1.6"/>
    <text class="bubble-text" x="60" y="209" font-size="12" text-anchor="middle">The</text>
    <text class="bubble-text" x="60" y="222" font-size="12" text-anchor="middle">Original</text>
    <rect x="100" y="196" width="150" height="38" rx="16" fill="var(--ink)" opacity="0.9" role="img" aria-label="Three chick illustrations"/>
    <text class="weight" x="29" y="268" font-size="27" textLength="149" lengthAdjust="spacingAndGlyphs">NET WT 2 OZ</text>
    <line x1="29" y1="271" x2="190" y2="271" stroke="var(--ink)" stroke-width="1"/>
    <text class="website" x="29" y="286" font-size="11" textLength="149" lengthAdjust="spacing">www.Spin4Rye.com</text>
    <circle cx="216" cy="263" r="25" fill="var(--ink)"/>
    <text class="brand-text" x="216" y="267" font-size="10" text-anchor="middle" fill="var(--soy)">Spin4Rye</text>
  </svg>

  <!-- Sweet Red Sauce -->
  <svg class="lid lid--black" viewBox="0 0 272 307" aria-label="Sweet Red Sauce lid">
    <rect width="272" height="307" rx="32" fill="var(--black)"/>
    <text class="headline" x="33" y="74" font-size="62" textLength="216" lengthAdjust="spacingAndGlyphs">SWEET</text>
    <text class="headline headline--accent" x="33" y="146" font-size="94" textLength="214" lengthAdjust="spacingAndGlyphs">RED</text>
    <text class="headline" x="33" y="189" font-size="54" textLength="214" lengthAdjust="spacingAndGlyphs">SAUCE</text>
    <ellipse cx="60" cy="212" rx="27" ry="19" fill="none" stroke="var(--red)" stroke-width="1.6"/>
    <text class="bubble-text" x="60" y="209" font-size="12" text-anchor="middle">The</text>
    <text class="bubble-text" x="60" y="222" font-size="12" text-anchor="middle">Original</text>
    <rect x="100" y="196" width="150" height="38" rx="16" fill="var(--red)" role="img" aria-label="Three chick illustrations"/>
    <text class="weight weight--accent" x="29" y="268" font-size="27" textLength="149" lengthAdjust="spacingAndGlyphs">NET WT 2 OZ</text>
    <line x1="29" y1="271" x2="190" y2="271" stroke="var(--ink)" stroke-width="1"/>
    <text class="website" x="29" y="286" font-size="11" textLength="149" lengthAdjust="spacing">www.Spin4Rye.com</text>
    <circle cx="216" cy="263" r="25" fill="var(--red)"/>
    <text class="brand-text" x="216" y="267" font-size="10" text-anchor="middle" fill="var(--ink)">Spin4Rye</text>
  </svg>

</main>
</body>
</html>
```